Willow Harbor Family Relief-buis card/stationary design for our non profit company
Have fun, be creative and lets see what you come up with!
Willow Harbor Family Relief-buis card/stationary design for our non profit company - Health
Creative Brief
Bright & Fun-filled
Dana Holloway
27415 Marlow Ave Ste#208 Tustin CA 92781
harborwr@brightpostmail.net
We have not yet decided our titles yet. In the meantime please focus on the design. Once we choose the design we want, we will ask you to put our names,title etc. Thank you!
Please put our tagline: "Supporting the care in caregiving" on the back of the card.

```html
<!DOCTYPE html>
<html lang="en">
<head>
<meta charset="utf-8">
<title>Willow Harbor Family Relief – Business Card</title>
<link rel="stylesheet" href="https://fonts.googleapis.com/css2?family=Montserrat:wght@400;500;600;700&display=swap">
<style>
  :root {
    --brand-blue: #1f5fae;
    --brand-blue-dark: #184d8f;
    --swoosh-grey: #a9adb3;
    --card-white: #ffffff;
    --ink: #3d4148;
    --ink-soft: #6b7078;
    --backdrop: #e9eaec;
  }
  * { margin: 0; padding: 0; box-sizing: border-box; }
  html, body { width: 1200px; height: 901px; overflow: hidden; }
  body {
    background: var(--backdrop);
    font-family: "Montserrat", Arial, sans-serif;
    display: flex; align-items: center; justify-content: center;
  }
  .business-card {
    position: relative;
    width: 960px; height: 560px;
    border-radius: 44px;
    background: var(--card-white);
    overflow: hidden;
    box-shadow: 0 18px 40px rgba(0,0,0,0.14);
  }
  .card-shapes { position: absolute; inset: 0; }
  .holder {
    position: absolute; left: 560px; top: 62px;
  }
  .holder-name {
    color: var(--brand-blue);
    font-weight: 700; font-size: 26px; letter-spacing: 1px;
    text-transform: uppercase;
  }
  .holder-title {
    color: var(--ink-soft);
    font-size: 15px; margin-top: 4px;
  }
  .contact-list {
    position: absolute; left: 560px; top: 138px;
    list-style: none;
  }
  .contact-item {
    display: flex; align-items: center; gap: 12px;
    color: var(--ink); font-size: 14px; height: 24px;
  }
  .contact-icon { width: 14px; height: 14px; flex: none; }
  .brand {
    position: absolute; left: 70px; top: 276px;
    display: flex; align-items: center; gap: 16px;
  }
  .brand-dot {
    width: 58px; height: 58px; border-radius: 50%;
    background: var(--brand-blue);
  }
  .brand-name {
    color: var(--brand-blue);
    font-weight: 600; font-size: 26px; line-height: 1.15;
    text-transform: uppercase; letter-spacing: 0.5px;
  }
  .address {
    position: absolute; left: 74px; top: 448px;
    color: var(--card-white);
    font-size: 22px; font-weight: 500; line-height: 1.35;
    letter-spacing: 0.5px;
  }
</style>
</head>
<body>
  <main class="business-card">
    <svg class="card-shapes" viewBox="0 0 960 560" width="960" height="560" aria-hidden="true">
      <path d="M0,392 C240,378 470,318 610,282 C750,246 870,224 960,222 L960,236 C870,240 750,262 612,300 C470,338 240,398 0,410 Z" fill="var(--swoosh-grey)"/>
      <path d="M0,420 C250,404 480,342 620,306 C760,270 880,250 960,248 L960,560 L0,560 Z" fill="var(--brand-blue)"/>
    </svg>

    <header class="holder">
      <h1 class="holder-name">Dana Holloway</h1>
      <p class="holder-title">Managing Director</p>
    </header>

    <ul class="contact-list">
      <li class="contact-item">
        <svg class="contact-icon" viewBox="0 0 16 16"><path d="M3 1h3l1.5 4-2 1.5a9 9 0 0 0 4 4L11 8.5l4 1.5v3a2 2 0 0 1-2 2A13 13 0 0 1 1 3a2 2 0 0 1 2-2z" fill="var(--ink)"/></svg>
        555 014 2290
      </li>
      <li class="contact-item">
        <svg class="contact-icon" viewBox="0 0 16 16"><rect x="4" y="1" width="8" height="14" rx="1.5" fill="var(--ink)"/><rect x="5.5" y="3" width="5" height="8" fill="#fff"/></svg>
        555 014 2291
      </li>
      <li class="contact-item">
        <svg class="contact-icon" viewBox="0 0 16 16"><rect x="1" y="5" width="14" height="8" rx="1" fill="var(--ink)"/><rect x="4" y="2" width="8" height="4" fill="var(--ink)"/><rect x="4" y="10" width="8" height="4" fill="#fff" stroke="var(--ink)"/></svg>
        555 014 2292
      </li>
      <li class="contact-item">
        <svg class="contact-icon" viewBox="0 0 16 16"><rect x="1" y="3" width="14" height="10" rx="1" fill="var(--ink)"/><path d="M1.5 4 8 9l6.5-5" stroke="#fff" fill="none" stroke-width="1.3"/></svg>
        harborwr@brightpostmail.net
      </li>
      <li class="contact-item">
        <svg class="contact-icon" viewBox="0 0 16 16"><circle cx="8" cy="8" r="7" fill="var(--brand-blue)"/><path d="M1 8h14M8 1c3 3 3 11 0 14M8 1c-3 3-3 11 0 14" stroke="#fff" fill="none"/></svg>
        www.harborwr.org
      </li>
    </ul>

    <div class="brand">
      <span class="brand-dot"></span>
      <p class="brand-name">Willow Harbor<br>Family Relief</p>
    </div>

    <address class="address" style="font-style:normal">
      27415 Marlow Ave Ste#208<br>Tustin CA 92781
    </address>
  </main>
</body>
</html>
```